Delwyn's Pressure Washing Services

Starting a pressure washing business on my own in Central Valley California, not too much experience so affordable, I do houses, fences, driveways, cars, trailers, RVs. Planning to make this full-time hoping clientele picks up after having a nice business card. Design doesn't have to be flashy, more to the point, I like simplistic/personable. I do not want something exhausting to look at or with too much going on.

Target Market(s)

Residential, Commercial

Industry/Entity Type

Pressure Washing

Contact Information for Business Card

avalible Services

Font styles to use
Sans Serif

Colors
0054AA
0677BA
7BADD7
CADEEF
E8F1F8
0094D4
00A9DD
6FCCEA
C7EBF8
E9F6FB
00AB8E
00BBA5
67D7C9
C6EFE9
E9F9F6

```html
<!DOCTYPE html>
<html lang="en">
<head>
<meta charset="utf-8">
<title>Delwyn's Pressure Washing Services – Business Card</title>
<link rel="stylesheet" href="https://fonts.googleapis.com/css2?family=Questrial&display=swap">
<style>
  :root {
    --brand-blue: #0054AA;
    --accent-blue: #0677BA;
    --soft-blue: #7BADD7;
    --pale-blue: #CADEEF;
    --mist: #E8F1F8;
    --ink: #1a1a1a;
    --paper: #ffffff;
    --backdrop: #eef1f4;
  }
  html, body {
    margin: 0;
    padding: 0;
    width: 1200px;
    height: 786px;
    overflow: hidden;
    background: var(--backdrop);
    font-family: "Questrial", "Century Gothic", sans-serif;
  }
  .business-card {
    position: absolute;
    left: 100px;
    top: 107px;
    width: 1000px;
    height: 572px;
    background: var(--brand-blue);
    box-shadow: 0 12px 32px rgba(0, 40, 90, 0.18);
    overflow: hidden;
  }
  .card-shapes {
    position: absolute;
    inset: 0;
    width: 100%;
    height: 100%;
  }
  .brand-name {
    position: absolute;
    left: 44px;
    top: 170px;
    width: 420px;
    color: var(--paper);
    margin: 0;
    font-weight: 400;
  }
  .brand-name .brand-main {
    display: block;
    font-size: 60px;
    letter-spacing: 2px;
    text-transform: uppercase;
    line-height: 1.05;
  }
  .brand-name .brand-sub {
    display: block;
    font-size: 19px;
    letter-spacing: 1px;
    text-transform: uppercase;
    margin-top: 6px;
  }
  .contact-block {
    position: absolute;
    right: 40px;
    top: 118px;
    text-align: right;
    color: var(--ink);
  }
  .person-name {
    margin: 0;
    font-size: 44px;
    font-weight: 400;
    letter-spacing: 2px;
    color: var(--brand-blue);
    text-transform: uppercase;
    line-height: 1;
  }
  .person-role {
    margin: 6px 0 0;
    font-size: 24px;
  }
  .address {
    margin: 76px 0 0;
    font-style: normal;
    font-size: 27px;
    line-height: 1.3;
  }
  .divider {
    width: 220px;
    height: 2px;
    background: var(--soft-blue);
    margin: 18px 0 18px auto;
  }
  .contact-list {
    list-style: none;
    margin: 0;
    padding: 0;
    font-size: 26px;
    line-height: 1.33;
  }
  .contact-list li {
    display: flex;
    justify-content: flex-end;
    align-items: center;
    gap: 10px;
  }
  .contact-icon {
    width: 20px;
    height: 20px;
    flex: none;
  }
</style>
</head>
<body>
  <article class="business-card">
    <svg class="card-shapes" viewBox="0 0 1000 572" preserveAspectRatio="none" aria-hidden="true">
      <defs>
        <linearGradient id="sheen" x1="0" y1="1" x2="1" y2="0">
          <stop offset="0" stop-color="#d7dde3"/>
          <stop offset="1" stop-color="#ffffff" stop-opacity="0"/>
        </linearGradient>
      </defs>
      <polygon points="690,0 1000,0 1000,505 990,538 200,538" fill="#ffffff"/>
      <polygon points="200,538 470,270 560,270 330,538" fill="url(#sheen)" opacity="0.8"/>
      <polygon points="330,538 560,300 640,300 450,538" fill="url(#sheen)" opacity="0.5"/>
      <line x1="670" y1="18" x2="320" y2="360" stroke="#7BADD7" stroke-width="2"/>
      <polygon points="1000,510 1000,528 975,560 955,560" fill="#0677BA"/>
      <line x1="240" y1="560" x2="680" y2="556" stroke="#7BADD7" stroke-width="1.5"/>
    </svg>

    <h1 class="brand-name">
      <span class="brand-main">Delwyn's</span>
      <span class="brand-sub">Pressure Washing Services</span>
    </h1>

    <section class="contact-block">
      <h2 class="person-name">Delwyn Marsh</h2>
      <p class="person-role">Owner</p>
      <address class="address">00 NW Harlan Ridge Drive<br>Modesto, CA 00000</address>
      <div class="divider"></div>
      <ul class="contact-list">
        <li>209 555 0148
          <svg class="contact-icon" viewBox="0 0 24 24" aria-hidden="true"><path d="M6.6 10.8a15 15 0 0 0 6.6 6.6l2.2-2.2a1 1 0 0 1 1-.25 11.4 11.4 0 0 0 3.6.57 1 1 0 0 1 1 1V20a1 1 0 0 1-1 1A17 17 0 0 1 3 4a1 1 0 0 1 1-1h3.5a1 1 0 0 1 1 1c0 1.25.2 2.45.57 3.57a1 1 0 0 1-.25 1z" fill="#7BADD7"/></svg>
        </li>
        <li>delwyn@delwynwash.com
          <svg class="contact-icon" viewBox="0 0 24 24" aria-hidden="true"><rect x="2" y="5" width="20" height="14" rx="1.5" fill="#7BADD7"/><path d="M3 6l9 7 9-7" stroke="#fff" stroke-width="1.6" fill="none"/></svg>
        </li>
        <li>www.delwynwash.com
          <svg class="contact-icon" viewBox="0 0 24 24" aria-hidden="true"><circle cx="12" cy="12" r="9.5" fill="#7BADD7"/><path d="M2.5 12h19M12 2.5c3 3 3 16 0 19M12 2.5c-3 3-3 16 0 19" stroke="#fff" stroke-width="1.4" fill="none"/></svg>
        </li>
      </ul>
    </section>
  </article>
</body>
</html>
```